Presentation Folder Cover For Plumbing Company

We need a presentation folder cover (FRONT AND BACK) for our plumbing business.

We specialise in plumbing, hot water, electrical and pipe relining.

This will be sent to clients and the contents pages will outline all of our company details and information.

The target market for this cover is Strata / Property Managers who look after unit buildings.

Target Market(s)

Strata & Property Managers. The higher end of the property market.

Industry/Entity Type

Plumbing

Font styles to use
Sans Serif

Colors
ec1f27
0355a3
ffffff
474747
c9c9c9

Requirements
Must have
• A4 Paper Size
• Inviting to clients to open the document and read on.
Nice to have
• Sleek, Professional and Stands Out.
Should not have
• Dark Background. Needs to be fresh and bright.

```html
<!DOCTYPE html>
<html lang="en">
<head>
<meta charset="utf-8">
<title>Dunmore Contracting – Presentation Folder</title>
<link href="https://fonts.googleapis.com/css2?family=Open+Sans:wght@400;600;700;800&display=swap" rel="stylesheet">
<style>
  :root{
    --red:#ec1f27;
    --blue:#0355a3;
    --blue-dark:#0a4a8f;
    --white:#ffffff;
    --charcoal:#474747;
    --silver:#c9c9c9;
    --paper:#f3f3f3;
    --stage:#e6e7e9;
    --trim:#6fc7e6;
    --cut:#e0282f;
    --fold:#59c08a;
  }
  *{margin:0;padding:0;box-sizing:border-box}
  html,body{width:1200px;height:1029px;overflow:hidden;background:var(--stage);font-family:"Open Sans",Arial,sans-serif}
  .canvas{position:relative;width:1200px;height:1029px}
  .dieline{position:absolute;left:0;top:0}
  .abs{position:absolute}

  .photo{position:absolute}
  .photo-kitchen{left:115px;top:99px;width:467px;height:454px;
    background:linear-gradient(160deg,#f4f6f7 0%,#e3e8ea 45%,#c9d0d6 70%,#3c4a6a 100%)}
  .photo-team{left:660px;top:244px;width:380px;height:309px;
    background:radial-gradient(ellipse at 50% 60%,#4a6a9a 0%,#6d86ab 35%,#dfe4ec 75%,transparent 100%)}

  .brand{position:absolute;text-align:center;color:var(--blue);font-weight:800;letter-spacing:.3px}
  .brand .mark{display:inline-block;background:var(--red);vertical-align:middle}
  .brand-name{white-space:nowrap}
  .brand-services{font-weight:600;color:#1a1a1a;letter-spacing:0;white-space:nowrap}
  .brand-small{left:355px;top:150px;width:210px}
  .brand-small .mark{width:11px;height:11px;margin-right:6px}
  .brand-small .brand-name{font-size:15px;line-height:20px}
  .brand-small .brand-services{font-size:11px;margin-top:36px}
  .brand-large{left:670px;top:148px;width:360px}
  .brand-large .mark{width:14px;height:14px;margin-right:8px}
  .brand-large .brand-name{font-size:27px;line-height:36px}
  .brand-large .brand-services{font-size:14px;margin-top:24px}

  .call-now{left:115px;top:564px;width:467px;text-align:center;color:var(--white);font-weight:800;font-size:27px;letter-spacing:.3px}
  .contact-line{left:115px;top:612px;width:467px;text-align:center;color:var(--white);font-weight:600;font-size:11px;display:flex;justify-content:center;gap:14px;align-items:center}
  .contact-line span{display:inline-flex;align-items:center;gap:5px}
  .specialise{left:617px;top:573px;width:468px;text-align:center;color:var(--white);font-weight:700;font-size:17px;line-height:22px}
  .web{font-size:13px;color:var(--blue);text-align:center;width:467px}
  .web b{font-weight:700}
  .web .hl{color:var(--red);font-weight:700}
  .web-left{left:115px;top:654px}
  .web-right{left:617px;top:654px}

  .welcome{left:628px;top:729px;width:428px;height:201px;transform:rotate(180deg);
    text-align:center;padding-top:48px;color:#222}
  .welcome h2{font-size:16px;font-weight:700;margin-bottom:8px}
  .welcome h2 .hl{color:var(--red)}
  .welcome h3{font-size:10px;font-weight:600;letter-spacing:.3px;margin-bottom:10px}
  .welcome p{font-size:8px;line-height:12px;margin:0 auto 8px;width:320px}
</style>
</head>
<body>
<div class="canvas">
  <svg class="dieline" width="1200" height="1029" viewBox="0 0 1200 1029">
    <path d="M57 88 L90 83 L1110 83 L1143 88 L1143 455 A18 18 0 0 0 1143 491 L1143 705 L1100 711 L1100 942 Q1100 948 1094 948 L660 948 Q646 948 640 934 L606 711 L599 711 L592 711 L565 934 Q560 948 545 948 L106 948 Q100 948 100 942 L100 711 L57 705 L57 491 A18 18 0 0 0 57 455 Z"
          fill="var(--paper)" stroke="var(--cut)" stroke-width="1"/>
    <path d="M100 711 L592 711 L565 934 Q560 948 545 948 L106 948 Q100 948 100 942 Z" fill="#f0f0f0"/>
    <path d="M606 711 L1100 711 L1100 942 Q1100 948 1094 948 L660 948 Q646 948 640 934 Z" fill="#f0f0f0"/>
    <line x1="599" y1="83" x2="599" y2="711" stroke="var(--fold)" stroke-width="1" stroke-dasharray="3 3"/>
    <line x1="57" y1="711" x2="1143" y2="711" stroke="var(--fold)" stroke-width="1" stroke-dasharray="3 3"/>
    <rect x="115" y="99" width="467" height="594" fill="var(--white)" stroke="var(--trim)" stroke-width="1"/>
    <rect x="617" y="99" width="468" height="594" fill="var(--white)" stroke="var(--trim)" stroke-width="1"/>
    <path d="M628 729 L1056 729 L1056 930 L668 930 Q650 930 645 912 Z" fill="var(--white)" stroke="var(--trim)" stroke-width="1"/>
    <g stroke="var(--cut)" stroke-width="1">
      <line x1="252" y1="807" x2="284" y2="775"/>
      <line x1="409" y1="775" x2="441" y2="807"/>
      <line x1="252" y1="853" x2="284" y2="885"/>
      <line x1="409" y1="885" x2="441" y2="853"/>
    </g>
    <polygon points="128,553 582,553 582,604 575,604 563,637 115,637 115,585" fill="var(--blue)"/>
    <polygon points="124,604 575,604 563,637 115,637" fill="var(--blue-dark)"/>
    <polygon points="637,553 1085,553 1065,637 617,637" fill="var(--red)"/>
  </svg>

  <div class="photo photo-kitchen" role="img" aria-label="Photo of a smiling plumber holding a pipe wrench in a bright white kitchen, tool bag at his side"></div>
  <div class="photo photo-team" role="img" aria-label="Photo of two tradesmen, one in a hard hat and tool belt, one in overalls holding pipe fittings"></div>

  <div class="brand brand-small">
    <div class="brand-name"><span class="mark"></span>Dunmore Contracting</div>
    <div class="brand-services">Plumbing • Electrical • Hot Water</div>
  </div>
  <div class="brand brand-large">
    <div class="brand-name"><span class="mark"></span>Dunmore Contracting</div>
    <div class="brand-services">Plumbing • Electrical • Hot Water</div>
  </div>

  <div class="abs call-now">CALL NOW - 180055 50 10</div>
  <div class="abs contact-line">
    <span><svg width="10" height="10" viewBox="0 0 10 10"><circle cx="5" cy="5" r="4.3" fill="none" stroke="#fff" stroke-width="1"/><path d="M3.4 3 L4.3 4.4 L3.9 4.9 Q4.6 6 5.4 6.3 L5.9 5.8 L7 6.6 L6.4 7.3 Q4.5 7 3 4 Z" fill="#fff"/></svg>02 5550 12 34</span>
    <span><svg width="10" height="10" viewBox="0 0 10 10"><rect x="3" y="1" width="4" height="3" fill="none" stroke="#fff"/><rect x="1" y="4" width="8" height="4" fill="#fff"/></svg>5550 1288</span>
    <span><svg width="11" height="8" viewBox="0 0 11 8"><rect x=".5" y=".5" width="10" height="7" fill="none" stroke="#fff"/><path d="M.5 .5 L5.5 4.5 L10.5 .5" fill="none" stroke="#fff"/></svg>service@dunmorecontracting.com.au</span>
  </div>
  <div class="abs specialise">WE SPECIALISE IN PLUMBING,<br>HOT WATER, ELECTRICAL AND PIPE RELINING.</div>

  <div class="abs web web-left">www.<b>dunmore</b><span class="hl">contracting</span>.com.au</div>
  <div class="abs web web-right">www.<b>dunmore</b><span class="hl">contracting</span>.com.au</div>

  <div class="abs welcome">
    <h2>Welcome to <span class="hl">Dunmore Contracting</span></h2>
    <h3>A SYDNEY BASED COMPANY, PROUDLY AUSTRALIAN OWNED</h3>
    <p>Dunmore Contracting Co Pty Ltd has been servicing Sydney for over 30yrs in the electrical and plumbing industry.</p>
    <p>Dunmore Contracting Co Pty Ltd strives to exceed your expectations with our commitment to provide 100% satisfaction and dependability at a fair price. Dunmore Contracting Co Pty Ltd has always based its business on customer satisfaction which in turn creates repeat business.</p>
  </div>
</div>
</body>
</html>
```